Garden Design Business Card Design

A business card design for garden design company called ;
ROOTED IN CLAY which has a great deal of maintenance but
wishes to promote its expertise for design in planting and garden
design, but in an informal manner.

Would love to see quite a rustic approach,very strong and innovative and taking risks on typography. Am open to ideas with
colours,as memorability is important.

Target Market(s)

General public 40/50 years in a very trendy area

Industry/Entity Type

Business

Contact Information for Business Card

ROOTED IN CLAY. Garden design and maintenance.
Peter Holcombe
Telephone 01632 960417 Mobile 07700 900382

```html
<!DOCTYPE html>
<html lang="en">
<head>
<meta charset="utf-8">
<title>Rooted in Clay – Business Card</title>
<link rel="stylesheet" href="https://fonts.googleapis.com/css2?family=Ubuntu:wght@300;500&display=swap">
<style>
  :root {
    --page-bg: #e9e9e7;
    --grass-light: #9cc46a;
    --grass-mid: #4f8a32;
    --grass-dark: #2a5420;
    --slate: #2f3848;
    --slate-deep: #262e3c;
    --card-text: #e3e5e8;
    --rule: #f1f2f3;
  }
  * { box-sizing: border-box; margin: 0; padding: 0; }
  html, body {
    width: 1200px;
    height: 1200px;
    overflow: hidden;
    background: var(--page-bg);
  }
  body {
    display: flex;
    align-items: center;
    justify-content: center;
    font-family: "Ubuntu", sans-serif;
  }
  .business-card {
    position: relative;
    width: 1000px;
    height: 600px;
    overflow: hidden;
    box-shadow: 0 10px 30px rgba(0,0,0,0.18);
  }
  .grass-photo {
    position: absolute;
    inset: 0;
    background:
      linear-gradient(160deg, var(--grass-light) 0%, var(--grass-mid) 45%, var(--grass-dark) 100%);
  }
  .name-band {
    position: absolute;
    left: 0;
    right: 0;
    top: 62px;
    height: 118px;
    background: var(--slate);
    display: flex;
    align-items: center;
    justify-content: flex-end;
    padding-right: 48px;
  }
  .company-name {
    font-weight: 500;
    font-size: 88px;
    letter-spacing: 1px;
    color: var(--card-text);
    line-height: 1;
  }
  .contact-panel {
    position: absolute;
    left: 44px;
    right: 64px;
    top: 222px;
    bottom: 18px;
    background: var(--slate);
  }
  .contact-details {
    position: absolute;
    left: 36px;
    top: 34px;
    list-style: none;
    color: var(--card-text);
    font-weight: 300;
    font-size: 40px;
    line-height: 54px;
    letter-spacing: 0.5px;
  }
  .bottom-band {
    position: absolute;
    left: 0;
    right: 64px;
    bottom: 18px;
    height: 84px;
    background: var(--slate-deep);
  }
  .accent-rule {
    position: absolute;
    left: 0;
    right: 64px;
    bottom: 86px;
    height: 8px;
    background: var(--rule);
  }
</style>
</head>
<body>
  <article class="business-card">
    <div class="grass-photo" role="img" aria-label="Close-up photograph of long green grass blades"></div>

    <header class="name-band">
      <h1 class="company-name">Rooted in Clay</h1>
    </header>

    <section class="contact-panel">
      <ul class="contact-details">
        <li class="tagline">Garden design and maintenance</li>
        <li class="person-name">Peter Holcombe</li>
        <li class="telephone">Telephone 01632 960417</li>
        <li class="mobile">Mobile 07700 900382</li>
      </ul>
    </section>

    <div class="bottom-band"></div>
    <div class="accent-rule"></div>
  </article>
</body>
</html>
```